Bref créative
Stationary/ Business Card for Innovative Law Firm
Brett Morrow Law
Bright & Fun-filled
Brett K. Morrow
Attorney & Counselor
P.O. Box 8261
Key West, FL 33041
brett@brettmorrowlawexample.com
www.brettmorrowlawexample.com

```html
<!DOCTYPE html>
<html lang="en">
<head>
<meta charset="utf-8">
<title>Brett Morrow Law — Stationery</title>
<link rel="stylesheet" href="https://fonts.googleapis.com/css2?family=Cinzel:wght@500&family=Open+Sans:wght@400;600&display=swap">
<style>
  :root {
    --backdrop: #ece7df;
    --paper: #ffffff;
    --brown: #5b3b27;
    --brown-dark: #3f2819;
    --green: #7d9b3b;
    --grey: #8b8b8b;
    --grey-dark: #6d6d6d;
    --ink: #4a4a4a;
    --faint: #e6e8dc;
    --shadow: 0 2px 6px rgba(0,0,0,.18);
  }
  * { margin: 0; padding: 0; box-sizing: border-box; }
  html, body { width: 1200px; height: 600px; overflow: hidden; }
  body { background: var(--backdrop); font-family: "Open Sans", sans-serif; color: var(--ink); position: relative; }

  .brand { display: flex; align-items: center; gap: 5px; }
  .brand-dot { border-radius: 50%; background: var(--green); flex: none; }
  .brand-name { font-family: "Cinzel", serif; font-weight: 500; color: var(--brown); line-height: 1; }
  .brand-tag { font-size: 4px; letter-spacing: .08em; color: var(--grey); text-transform: uppercase; margin-top: 2px; }

  /* business cards */
  .card { position: absolute; left: 20px; width: 108px; height: 62px; background: var(--paper); box-shadow: var(--shadow); overflow: hidden; }
  .card-front { top: 187px; }
  .card-back { top: 290px; background: var(--brown); }
  .card .brand { position: absolute; left: 8px; top: 10px; }
  .card .brand-dot { width: 12px; height: 12px; }
  .card .brand-name { font-size: 7px; }
  .card-back .brand-name { color: var(--paper); }
  .card-band { position: absolute; left: 0; bottom: 0; width: 100%; height: 22px; }
  .card-contact { position: absolute; right: 6px; bottom: 4px; font-size: 3.4px; color: var(--paper); text-align: right; line-height: 1.4; }
  .card-back .card-band { height: 34px; }
  .card-back .card-panel { position: absolute; left: 0; top: 0; width: 100%; height: 30px; }
  .card-back .brand { z-index: 1; }
  .card-back .brand-name { color: var(--brown); }

  /* letterhead */
  .letterhead { position: absolute; left: 220px; top: 29px; width: 410px; height: 528px; background: var(--paper); box-shadow: var(--shadow); overflow: hidden; }
  .letterhead .brand { position: absolute; left: 24px; top: 22px; }
  .letterhead .brand-dot { width: 26px; height: 26px; }
  .letterhead .brand-name { font-size: 15px; }
  .letterhead .brand-tag { font-size: 5px; }
  .letterhead-contact { position: absolute; right: 26px; top: 24px; font-size: 5px; line-height: 1.5; color: var(--grey-dark); text-align: right; }
  .watermark-circle { position: absolute; right: 26px; bottom: 52px; width: 150px; height: 150px; border-radius: 50%; border: 9px solid var(--faint); }
  .letterhead-band { position: absolute; left: 0; bottom: 0; width: 100%; height: 70px; }

  /* envelopes */
  .envelope { position: absolute; background: var(--paper); box-shadow: var(--shadow); overflow: hidden; }
  .envelope-flap { position: absolute; left: 0; top: 0; width: 100%; height: 100%; }
  .env-back-brown { left: 700px; top: 24px; width: 450px; height: 190px; }
  .env-back-grey { left: 685px; top: 132px; width: 465px; height: 160px; }
  .env-back-white { left: 703px; top: 240px; width: 447px; height: 112px; }
  .env-front { left: 653px; top: 352px; width: 497px; height: 205px; }
  .env-front .brand { position: absolute; left: 22px; top: 22px; }
  .env-front .brand-dot { width: 20px; height: 20px; }
  .env-front .brand-name { font-size: 12px; }
  .env-return { position: absolute; left: 22px; top: 70px; font-size: 5px; color: var(--grey-dark); }
  .env-front .watermark-circle { right: 30px; bottom: 18px; width: 118px; height: 118px; border-width: 7px; }
</style>
</head>
<body>

  <!-- business card front -->
  <section class="card card-front">
    <div class="brand">
      <span class="brand-dot"></span>
      <div><div class="brand-name">Brett Morrow Law</div><div class="brand-tag">Attorney &amp; Counselor</div></div>
    </div>
    <svg class="card-band" viewBox="0 0 108 22" preserveAspectRatio="none" aria-hidden="true">
      <path d="M0 10 Q54 -2 108 10 V22 H0 Z" fill="var(--brown)"/>
    </svg>
    <div class="card-contact">Brett K. Morrow · P.O. Box 8261, Key West, FL 33041<br>brett@brettmorrowlawexample.com</div>
  </section>

  <!-- business card back -->
  <section class="card card-back">
    <svg class="card-panel" viewBox="0 0 108 30" preserveAspectRatio="none" aria-hidden="true">
      <path d="M0 0 H108 V24 Q54 34 0 24 Z" fill="var(--paper)"/>
    </svg>
    <div class="brand">
      <span class="brand-dot"></span>
      <div class="brand-name">Brett Morrow Law</div>
    </div>
    <div class="card-contact">www.brettmorrowlawexample.com</div>
  </section>

  <!-- letterhead -->
  <section class="letterhead">
    <div class="brand">
      <span class="brand-dot"></span>
      <div><div class="brand-name">Brett Morrow Law</div><div class="brand-tag">Attorney &amp; Counselor</div></div>
    </div>
    <div class="letterhead-contact">
      P.O. Box 8261, Key West, FL 33041<br>
      brett@brettmorrowlawexample.com<br>
      www.brettmorrowlawexample.com
    </div>
    <div class="watermark-circle"></div>
    <svg class="letterhead-band" viewBox="0 0 410 70" preserveAspectRatio="none" aria-hidden="true">
      <path d="M0 28 Q205 -6 410 28 V70 H0 Z" fill="var(--brown)"/>
      <path d="M0 28 Q205 -6 410 28 V34 Q205 2 0 34 Z" fill="var(--brown-dark)"/>
    </svg>
  </section>

  <!-- envelope backs -->
  <div class="envelope env-back-brown">
    <svg class="envelope-flap" viewBox="0 0 450 190" preserveAspectRatio="none" aria-hidden="true">
      <path d="M0 0 H450 V40 L250 118 Q225 126 200 118 L0 40 Z" fill="var(--brown)"/>
    </svg>
  </div>
  <div class="envelope env-back-grey">
    <svg class="envelope-flap" viewBox="0 0 465 160" preserveAspectRatio="none" aria-hidden="true">
      <path d="M0 0 H465 V34 L258 96 Q232 104 206 96 L0 34 Z" fill="var(--grey)"/>
    </svg>
  </div>
  <div class="envelope env-back-white">
    <svg class="envelope-flap" viewBox="0 0 447 112" preserveAspectRatio="none" aria-hidden="true">
      <path d="M0 0 H447 V26 L248 80 Q223 87 198 80 L0 26 Z" fill="#f3f3f3"/>
    </svg>
  </div>

  <!-- envelope front -->
  <section class="envelope env-front">
    <div class="brand">
      <span class="brand-dot"></span>
      <div><div class="brand-name">Brett Morrow Law</div><div class="brand-tag">Attorney &amp; Counselor</div></div>
    </div>
    <div class="env-return">P.O. Box 8261, Key West, FL 33041</div>
    <div class="watermark-circle"></div>
  </section>

</body>
</html>
```